Business Card Design Project

Hi,
This is a simple contest. The logo for the back of the card is deigned. See attached files. The front of the card must have :

Directors Name: Dorian
Mob:
e-mail:
Postal Address:
Web Page Adress:

It may also add words: "Leaders in Construction Project Management Services"

Target Market(s)

Business & Home owners alike

Industry/Entity Type

Business

Requirements
Must have
• See details above and logo attached
Should not have
• Images other than logo

```html
<!DOCTYPE html>
<html lang="en">
<head>
<meta charset="UTF-8">
<title>Keystone Build Group – Business Cards</title>
<link href="https://fonts.googleapis.com/css2?family=Montserrat:wght@400;500;700;800&display=swap" rel="stylesheet">
<style>
  :root {
    --brand-blue: #2f9be0;
    --brand-blue-light: #a9d4f2;
    --paper: #ffffff;
    --backdrop: #e4e5e7;
    --ink-grey: #8a9199;
  }
  html, body {
    margin: 0;
    padding: 0;
    width: 1200px;
    height: 900px;
    overflow: hidden;
    background: var(--backdrop);
    font-family: "Montserrat", sans-serif;
  }
  .canvas {
    position: relative;
    width: 1200px;
    height: 900px;
  }
  .card {
    position: absolute;
    width: 540px;
    height: 310px;
    overflow: hidden;
    box-shadow: 0 10px 24px rgba(0,0,0,0.12);
  }
  .card-front { left: 80px; top: 110px; background: var(--paper); }
  .card-back  { left: 580px; top: 470px; background: var(--brand-blue); }

  .card-shapes { position: absolute; inset: 0; width: 100%; height: 100%; }

  .wordmark {
    position: absolute;
    display: flex;
    align-items: center;
    gap: 12px;
    font-weight: 800;
    text-transform: uppercase;
  }
  .wordmark-square {
    width: 38px;
    height: 38px;
    background: currentColor;
  }
  .wordmark-text { line-height: 1; }
  .wordmark-main { display: block; font-size: 34px; letter-spacing: 1px; }
  .wordmark-sub  { display: block; font-size: 11px; letter-spacing: 4.6px; margin-top: 4px; }

  .card-front .wordmark { left: 40px; top: 118px; color: var(--brand-blue); }
  .card-back .wordmark  { left: 50%; top: 50%; transform: translate(-50%, -50%); color: var(--paper); }

  .holder {
    position: absolute;
    right: 40px;
    top: 30px;
    text-align: right;
  }
  .holder-name {
    margin: 0;
    font-size: 18px;
    font-weight: 800;
    letter-spacing: 1px;
    color: var(--brand-blue);
    text-transform: uppercase;
  }
  .holder-title {
    margin: 3px 0 0;
    font-size: 8px;
    font-weight: 500;
    letter-spacing: 1.5px;
    color: var(--ink-grey);
    text-transform: uppercase;
  }

  .contact-list {
    position: absolute;
    left: 40px;
    right: 100px;
    bottom: 30px;
    margin: 0;
    padding: 0;
    list-style: none;
    display: grid;
    grid-template-columns: 1fr 1.5fr;
    gap: 10px 18px;
  }
  .contact-item {
    display: flex;
    align-items: center;
    gap: 8px;
    font-size: 9.5px;
    font-weight: 500;
    color: var(--ink-grey);
    white-space: nowrap;
  }
  .contact-icon {
    width: 16px;
    height: 16px;
    flex: none;
  }
</style>
</head>
<body>
<main class="canvas">

  <section class="card card-front" aria-label="Business card front">
    <svg class="card-shapes" viewBox="0 0 540 310" preserveAspectRatio="none" aria-hidden="true">
      <polygon points="490,170 540,120 540,310 490,310" fill="var(--brand-blue)"/>
      <polygon points="462,200 474,188 474,310 462,310" fill="var(--brand-blue-light)"/>
      <polygon points="0,0 60,0 60,40 0,100" fill="var(--brand-blue)"/>
      <polygon points="70,0 82,0 82,30 70,42" fill="var(--brand-blue-light)"/>
    </svg>

    <div class="holder">
      <p class="holder-name">Dorian</p>
      <p class="holder-title">Director</p>
    </div>

    <div class="wordmark">
      <span class="wordmark-square" aria-hidden="true"></span>
      <span class="wordmark-text">
        <span class="wordmark-main">Keystone</span>
        <span class="wordmark-sub">Build Group</span>
      </span>
    </div>

    <ul class="contact-list">
      <li class="contact-item">
        <svg class="contact-icon" viewBox="0 0 16 16" aria-hidden="true"><circle cx="8" cy="8" r="8" fill="var(--brand-blue)"/><path d="M5.5 4.5l1.5 0 .7 1.8-.9.7a5 5 0 0 0 2.2 2.2l.7-.9 1.8.7v1.5c0 .4-.4.8-.8.7A6.5 6.5 0 0 1 4.8 5.3c0-.4.3-.8.7-.8z" fill="#fff"/></svg>
        0400 123 456
      </li>
      <li class="contact-item">
        <svg class="contact-icon" viewBox="0 0 16 16" aria-hidden="true"><circle cx="8" cy="8" r="8" fill="var(--brand-blue)"/><circle cx="8" cy="8" r="3.6" fill="none" stroke="#fff" stroke-width="1.2"/><path d="M4.4 8h7.2M8 4.4c1.3 1.2 1.3 6 0 7.2M8 4.4c-1.3 1.2-1.3 6 0 7.2" stroke="#fff" stroke-width="0.8" fill="none"/></svg>
        www.keystonebuild.com
      </li>
      <li class="contact-item">
        <svg class="contact-icon" viewBox="0 0 16 16" aria-hidden="true"><circle cx="8" cy="8" r="8" fill="var(--brand-blue)"/><rect x="4" y="5.2" width="8" height="5.6" fill="none" stroke="#fff" stroke-width="1"/><path d="M4 5.4l4 3 4-3" fill="none" stroke="#fff" stroke-width="1"/></svg>
        info@keystonebuild.com
      </li>
      <li class="contact-item">
        <svg class="contact-icon" viewBox="0 0 16 16" aria-hidden="true"><circle cx="8" cy="8" r="8" fill="var(--brand-blue)"/><path d="M8 12.5s3-3.2 3-5.5a3 3 0 0 0-6 0c0 2.3 3 5.5 3 5.5z" fill="#fff"/><circle cx="8" cy="7" r="1.1" fill="var(--brand-blue)"/></svg>
        PO Box 210, Harbour Street, Adelaide SA
      </li>
    </ul>
  </section>

  <section class="card card-back" aria-label="Business card back">
    <svg class="card-shapes" viewBox="0 0 540 310" preserveAspectRatio="none" aria-hidden="true">
      <polygon points="430,0 540,0 540,90 470,90 430,50" fill="var(--paper)"/>
      <polygon points="0,230 70,230 110,270 110,310 0,310" fill="var(--paper)"/>
    </svg>
    <div class="wordmark">
      <span class="wordmark-square" aria-hidden="true"></span>
      <span class="wordmark-text">
        <span class="wordmark-main">Keystone</span>
        <span class="wordmark-sub">Build Group</span>
      </span>
    </div>
  </section>

</main>
</body>
</html>
```